Love-Drama Movie Flyer for World Sales Pitch

Dear Designers

We need for a world sales pitch a flyer for our new movie MARBLEFIN. We need a front and a back page A4.
Front: One picture we deliver for then whole page, title, some "pitch" sentences
Picture Front: https://www.fileharbor-example.net/s/qk83tnb2px71vd9/Front_Picture.jpg?dl=0
Back: Arrangement of title, 5 pictures and text we deliver (attached)

Please find in the attached examples a rough idea what we’re looking for. Should not be exactly the same.

To get an Impression of the content and style of the film, please watch the 3min teaser. This will be very important for the style of the flyer:
https://clipvault-example.net/487316920
pw: tutumarblefin

In the end we prefer a data package with the flyer made in a adobe design application for high quality print.

Thanks
Tomas Vrelnik
Producer

Target Market(s)

High profile film sales professionals

Industry/Entity Type

Film Production

Requirements
Must have
• see description
Should not have
• not too generic,
• there is the color red on the actors pullover but red is not really a color in the film. So please don't use much red
• Awards of the actor/actress are not for this movie, it's from other movies

```html
<!DOCTYPE html>
<html lang="en">
<head>
<meta charset="utf-8">
<title>MARBLEFIN – Flyer</title>
<link rel="stylesheet" href="https://fonts.googleapis.com/css2?family=Oswald:wght@300;400;500&family=Arimo:wght@400;700&display=swap">
<style>
  :root {
    --bg: #0c0c0d;
    --page-dark: #0e1418;
    --ink: #ffffff;
    --ink-soft: #d9dde0;
    --ink-muted: #a9b0b5;
    --band: #3a3d40;
    --photo-teal: #3f7f8c;
    --photo-deep: #13242c;
  }
  * { margin: 0; padding: 0; box-sizing: border-box; }
  html, body { width: 1200px; height: 848px; overflow: hidden; background: var(--bg); }
  .canvas { position: relative; width: 1200px; height: 848px; background: var(--bg); }

  .page { position: absolute; top: 36px; width: 546px; height: 771px; overflow: hidden; }
  .page--front { left: 46px; }
  .page--back { left: 606px; background: var(--page-dark); }

  .front-photo {
    position: absolute; inset: 0;
    background:
      radial-gradient(ellipse at 78% 55%, rgba(120,175,185,.55), transparent 55%),
      linear-gradient(90deg, #2a2622 0%, #4b4a47 22%, #2c3a40 45%, #3b6670 70%, #2a4a55 100%);
  }

  .billing { position: absolute; right: 18px; top: 22px; width: 260px; text-align: right; font-family: 'Oswald', sans-serif; color: var(--ink); text-transform: uppercase; }
  .billing__star { font-size: 30px; font-weight: 400; line-height: 1; }
  .billing__star small { font-size: 15px; margin-right: 2px; }
  .credits { display: flex; justify-content: flex-end; gap: 8px; margin-top: 4px; }
  .credit { display: flex; flex-direction: column; align-items: flex-end; line-height: 1.05; }
  .credit__label { font-size: 11px; color: var(--ink-soft); }
  .credit__tiny { font-size: 6px; color: var(--ink-muted); }
  .credit__big { font-size: 18px; }
  .credit__year { font-size: 16px; }
  .billing__star--second { margin-top: 16px; }

  .tagline { position: absolute; left: 276px; top: 326px; font-family: 'Oswald', sans-serif; font-size: 34px; line-height: 1.32; color: var(--ink); }

  .title-block { position: absolute; left: 0; right: 0; top: 560px; text-align: center; font-family: 'Oswald', sans-serif; color: var(--ink); }
  .title { font-size: 92px; font-weight: 500; line-height: 1; letter-spacing: 1px; }
  .director { font-size: 17px; font-weight: 300; margin-top: 4px; }
  .release { font-size: 21px; font-weight: 500; margin-top: 12px; }
  .site { font-size: 12px; letter-spacing: 3px; margin-top: 12px; }

  .still { position: absolute; background: linear-gradient(135deg, var(--photo-deep), var(--photo-teal)); }
  .still--1 { left: 64px; top: 20px; width: 204px; height: 130px; background: linear-gradient(135deg, #2b3432, #6f7a70); }
  .still--2 { left: 276px; top: 20px; width: 204px; height: 130px; background: linear-gradient(135deg, #27343a, #5f7278); }
  .still--3 { left: 109px; top: 158px; width: 323px; height: 170px; background: radial-gradient(ellipse at 70% 10%, #6fb7c9, #1f5a6b 55%, #0f2c36); }
  .still--4 { left: 64px; top: 338px; width: 204px; height: 130px; background: linear-gradient(135deg, #c7c1b3, #5e5a54); }
  .still--5 { left: 276px; top: 338px; width: 204px; height: 130px; background: linear-gradient(135deg, #5d6a72, #c28a52); }

  .synopsis { position: absolute; left: 24px; right: 24px; top: 486px; text-align: center; font-family: 'Arimo', sans-serif; font-size: 9.6px; line-height: 1.45; color: var(--ink-soft); }
  .synopsis p + p { margin-top: 10px; }

  .specs { position: absolute; left: 0; right: 0; top: 643px; height: 42px; background: var(--band); text-align: center; font-family: 'Arimo', sans-serif; font-size: 8.6px; line-height: 1.4; color: var(--ink-soft); padding-top: 5px; }

  .contact { position: absolute; left: 0; right: 0; top: 692px; text-align: center; font-family: 'Arimo', sans-serif; font-size: 6.6px; line-height: 1.45; color: var(--ink-muted); }
  .contact__head { font-weight: 700; font-size: 7.5px; color: var(--ink-soft); }
</style>
</head>
<body>
<main class="canvas">
  <section class="page page--front">
    <div class="front-photo" role="img" aria-label="Hooded young man in close-up on the left, a woman at a misty window behind him, teal and grey tones"></div>

    <div class="billing">
      <div class="billing__star"><small>Starring</small>Lars Brenner</div>
      <div class="credits">
        <div class="credit"><span class="credit__label">Rising</span><span class="credit__label">Star</span><span class="credit__year">2015</span></div>
        <div class="credit"><span class="credit__tiny">Recurring appearance</span><span class="credit__tiny">in the award winning series</span><span class="credit__big">"Harbor Line"</span><span class="credit__label">Best Actor</span><span class="credit__tiny">-The Orbit-</span><span class="credit__label">National</span><span class="credit__year">2015</span></div>
      </div>
      <div class="billing__star billing__star--second">Mila Hartwig</div>
      <div class="credits">
        <div class="credit"><span class="credit__label">Best Actress</span><span class="credit__tiny">-Clara-</span><span class="credit__label">Fresh Faces</span><span class="credit__tiny">Award</span><span class="credit__year">2012</span></div>
        <div class="credit"><span class="credit__label">Best Actress</span><span class="credit__tiny">-Some Girl-</span><span class="credit__big">Meridian</span><span class="credit__tiny">Award nominee</span><span class="credit__year">2016</span><span class="credit__label">Best Young Actress</span><span class="credit__tiny">-Some Girl-</span><span class="credit__label">Alpine</span><span class="credit__tiny">Film Award</span><span class="credit__year">2015</span></div>
      </div>
    </div>

    <div class="tagline">THIS<br>IS<br>DAVID.</div>

    <div class="title-block">
      <h1 class="title">MARBLEFIN</h1>
      <div class="director">A FILM BY JONAS FERLACH</div>
      <div class="release">COMING FALL 2016</div>
      <div class="site">WWW.OSTRAND-FILMS.EXAMPLE</div>
    </div>
  </section>

  <section class="page page--back">
    <div class="still still--1" role="img" aria-label="Young man in a hoodie holding a newborn baby in a hallway"></div>
    <div class="still still--2" role="img" aria-label="Young woman with painted face in a dim corridor"></div>
    <div class="still still--3" role="img" aria-label="Two figures sinking underwater, light from above"></div>
    <div class="still still--4" role="img" aria-label="Man injecting in a bathroom while a pregnant woman stands behind"></div>
    <div class="still still--5" role="img" aria-label="Man lifting weights on a gym bench"></div>

    <div class="synopsis">
      <p>After nuclear plant worker DAVID (24) and his pregnant girlfriend JESSY (22) are beaten up,<br>David starts using steroids. But instead of being able to protect his girl and unborn baby,<br>he is becoming a threat to them. When the amateur bodybuilder loses control of his temper<br>and brutally beats her, she leaves him. Only when David abducts his newborn daughter from the<br>hospital, he becomes aware of his maniac behavior. He returns the baby and asks Jessy for forgiveness.<br>Two months later she shows up at his new workplace.</p>
      <p>After his debut in the award-winning gay-drama THE ORBIT, Lars Brenner shines alongside<br>German shooting star Mila Hartwig in the second feature of Switzerlands most promising<br>new director Jonas Ferlach.</p>
    </div>

    <div class="specs">
      DARK ROMANCE | 100 MIN | COLOR | SWISS-GERMAN/GERMAN<br>
      KESTREL CINE | 1:1,85 | VELORA SURROUND | BUDGET: EUR 1.5 MIO<br>
      https://clipvault-example.net/ostrandfilms/marblefin | Password: marblefin2016
    </div>

    <div class="contact">
      <div class="contact__head">CONTACT:</div>
      Ostrand Films<br>
      Tomas Vrelnik | Nina Aebli<br>
      Lindenweg 14 | 8004 Zurich | Switzerland<br>
      Phone: +41 79 000 12 34<br>
      info@ostrandfilms.example | www.ostrand-films.example
    </div>
  </section>
</main>
</body>
</html>
```